Corvanta512 Business Card Redesign

I want to create a design for brand new business cards, I need something exceptional for clear plastic business card design. Please do not submit without it being on a clear design. Photos of the various logo versions attached.

```html
<!DOCTYPE html>
<html lang="en">
<head>
<meta charset="utf-8">
<title>Corvanta512 – Clear Business Card</title>
<link href="https://fonts.googleapis.com/css2?family=Montserrat:wght@400;500;600;700&display=swap" rel="stylesheet">
<style>
  :root {
    --backdrop: #d9d4cc;
    --card-frost: rgba(255, 255, 255, 0.72);
    --card-edge: rgba(120, 112, 100, 0.45);
    --gold: #c29a45;
    --ink: #262626;
    --icon: #3b4a66;
  }
  * { margin: 0; padding: 0; box-sizing: border-box; }
  html, body {
    width: 1200px; height: 964px; overflow: hidden;
    background: var(--backdrop);
    font-family: "Montserrat", Arial, sans-serif;
  }
  .canvas { position: relative; width: 1200px; height: 964px; }
  .card {
    position: absolute; left: 100px; top: 196px;
    width: 1000px; height: 572px;
    background: var(--card-frost);
    border: 2px solid var(--card-edge);
    border-radius: 40px;
    overflow: hidden;
  }
  .name-marker {
    position: absolute; left: 0; top: 74px;
    width: 28px; height: 57px; background: var(--gold);
  }
  .holder { position: absolute; left: 54px; top: 68px; }
  .holder-name {
    font-weight: 700; font-size: 35px; letter-spacing: 0.5px;
    color: var(--gold); line-height: 1.1;
  }
  .holder-title {
    font-weight: 500; font-size: 25px; color: var(--ink); line-height: 1.2;
  }
  .divider-row {
    position: absolute; left: 54px; right: 0; top: 284px;
    display: flex; align-items: center; gap: 14px;
  }
  .divider { height: 2px; background: var(--gold); }
  .divider.lead { flex: 1; }
  .divider.tail { width: 56px; }
  .brand-name {
    font-weight: 600; font-size: 40px; color: var(--gold);
    line-height: 1; white-space: nowrap;
  }
  .address {
    position: absolute; left: 54px; top: 356px;
    font-size: 24px; font-weight: 500; color: var(--ink); line-height: 31px;
  }
  .contacts {
    position: absolute; left: 54px; top: 425px; list-style: none;
  }
  .contacts li {
    display: flex; align-items: center; gap: 10px;
    font-size: 24px; font-weight: 500; color: var(--ink);
    height: 38px;
  }
  .contacts svg { width: 18px; height: 18px; flex: none; fill: var(--icon); }
</style>
</head>
<body>
<div class="canvas">
  <div class="card">
    <div class="name-marker"></div>
    <div class="holder">
      <div class="holder-name">DELMAR QUINCEY</div>
      <div class="holder-title">CEO/Founder</div>
    </div>

    <div class="divider-row">
      <div class="divider lead"></div>
      <div class="brand-name">Corvanta512</div>
      <div class="divider tail"></div>
    </div>

    <div class="address">
      4170 Harbor Lane<br>
      Westfield AB 61830
    </div>

    <ul class="contacts">
      <li>
        <svg viewBox="0 0 24 24" aria-hidden="true"><path d="M6.6 10.8a15 15 0 0 0 6.6 6.6l2.2-2.2a1 1 0 0 1 1-.25 11.4 11.4 0 0 0 3.6.57 1 1 0 0 1 1 1V20a1 1 0 0 1-1 1A17 17 0 0 1 3 4a1 1 0 0 1 1-1h3.5a1 1 0 0 1 1 1c0 1.25.2 2.45.57 3.57a1 1 0 0 1-.25 1z"/></svg>
        (555) 310 482
      </li>
      <li>
        <svg viewBox="0 0 24 24" aria-hidden="true"><path d="M2 5h20v14H2z" fill="none"/><path d="M2 6l10 7 10-7v12H2z"/><path d="M2 5h20l-10 7z"/></svg>
        info@corvanta512.com
      </li>
      <li>
        <svg viewBox="0 0 24 24" aria-hidden="true"><path d="M12 2a10 10 0 1 0 0 20 10 10 0 0 0 0-20zm6.9 6h-2.9a15.7 15.7 0 0 0-1.4-3.6A8 8 0 0 1 18.9 8zM12 4c.8 1.2 1.5 2.5 1.9 4h-3.8c.4-1.5 1.1-2.8 1.9-4zM4.3 14a8 8 0 0 1 0-4h3.4a16.5 16.5 0 0 0 0 4zm.8 2h2.9c.3 1.3.8 2.5 1.4 3.6A8 8 0 0 1 5.1 16zM8 8H5.1a8 8 0 0 1 4.3-3.6C8.8 5.5 8.3 6.7 8 8zm4 12c-.8-1.2-1.5-2.5-1.9-4h3.8c-.4 1.5-1.1 2.8-1.9 4zm2.3-6H9.7a14.7 14.7 0 0 1 0-4h4.6a14.7 14.7 0 0 1 0 4zm.3 5.6c.6-1.1 1.1-2.3 1.4-3.6h2.9a8 8 0 0 1-4.3 3.6zM16.3 14a16.5 16.5 0 0 0 0-4h3.4a8 8 0 0 1 0 4z"/></svg>
        www.corvanta512.com
      </li>
    </ul>
  </div>
</div>
</body>
</html>
```